Report Design

I am looking for a redesign of our monthly inspection reports we submit to our customers. I uploaded the current one we use (FernHollow) and also that of a competitor (Calm Ridge). I want to more copy the layout of the Calmridge report I attached but with more flow and design.

Requirements
Must have
• This has to be in a template format that we can modify the content every month.

```html
<!DOCTYPE html>
<html lang="en">
<head>
<meta charset="utf-8">
<title>FernHollow – Monthly Inspection Report Template</title>
<link rel="stylesheet" href="https://fonts.googleapis.com/css2?family=Poppins:ital,wght@0,400;0,500;0,600;0,700;1,400&display=swap">
<style>
:root{
  --green-dark:#1f7a34;
  --green:#2ca843;
  --green-band:#22a03c;
  --black:#111;
  --text:#222;
  --paper:#fff;
  --bg-top:#8c8c8c;
  --bg-mid:#4a4a4a;
  --footer-gray:#c9c9c9;
  --grass:#efefef;
}
*{box-sizing:border-box;margin:0;padding:0}
html,body{width:890px;height:1200px;overflow:hidden}
body{
  font-family:"Poppins",sans-serif;
  background:linear-gradient(180deg,var(--bg-top) 0%,var(--bg-mid) 50%,var(--bg-top) 100%);
  position:relative;
}
.page{
  position:absolute;width:395px;height:511px;background:var(--paper);
  box-shadow:0 2px 8px rgba(0,0,0,.35);overflow:hidden;
}
.p1{left:34px;top:77px}
.p2{left:456px;top:77px}
.p3{left:34px;top:625px}
.p4{left:456px;top:625px}
.abs{position:absolute}

/* first page header */
.brand-band{
  left:128px;top:0;width:267px;height:56px;background:var(--green-dark);
  clip-path:polygon(0 0,100% 0,100% 100%,18% 100%);
}
.contact{left:195px;top:9px;color:#fff;font-size:6.4px;line-height:8.8px}
.contact .division{font-weight:700;font-size:6.6px}
.contact svg{width:5px;height:5px;vertical-align:-0.5px;margin-right:2px}
.brand-name{left:16px;top:40px;font-size:19px;font-weight:700;color:var(--green-dark);display:flex;align-items:center;gap:6px}
.brand-name .dot{width:12px;height:12px;border-radius:50%;background:var(--green)}

/* report title block */
.title{font-size:12.6px;font-weight:700;color:var(--green-dark);letter-spacing:.1px;white-space:nowrap}
.month{
  width:89px;height:20px;background:var(--green);color:#fff;font-weight:700;font-size:11px;
  display:flex;align-items:center;justify-content:center;
  clip-path:polygon(8% 0,100% 0,92% 100%,0 100%);
}
.subband{
  left:0;width:372px;height:20px;background:var(--green-band);color:#fff;
  font-weight:600;font-size:11.6px;display:flex;align-items:center;padding-left:16px;
  clip-path:polygon(0 0,94% 0,100% 100%,0 100%);
}
.subband::before{content:"";border-left:7px solid #fff;border-top:4.5px solid transparent;border-bottom:4.5px solid transparent;margin-right:5px}

/* inspection items */
.item-icon{
  width:42px;height:42px;border-radius:50%;background:#fff;border:2px solid var(--green);
  display:flex;align-items:center;justify-content:center;z-index:2;
}
.item-icon span{width:32px;height:32px;border-radius:50%;background:var(--green);display:flex;align-items:center;justify-content:center}
.item-icon svg{width:20px;height:20px}
.item-bar{
  width:196px;height:20px;background:var(--black);color:#fff;font-weight:700;font-size:11px;
  display:flex;align-items:center;padding-left:11px;
  clip-path:polygon(0 0,100% 0,92% 100%,0 100%);
}
.item-bar::after{content:"";position:absolute;right:0;top:0;width:14px;height:20px;background:var(--green);clip-path:polygon(60% 0,100% 0,40% 100%,0 100%)}
.item-text{font-size:7.4px;line-height:9px;color:var(--text);width:318px}
.photo{border:1px solid #bdbdbd}

/* footer */
.grass{left:70px;bottom:13px;width:325px;height:40px;background:linear-gradient(180deg,rgba(239,239,239,0) 0%,var(--grass) 100%)}
.footer-bar{left:70px;bottom:0;width:325px;height:13px;background:var(--footer-gray);display:flex;align-items:center;padding-left:12px;font-size:5px;font-style:italic;color:#333}
.page-no{right:0;bottom:0;width:34px;height:13px;background:var(--green);color:#fff;font-size:7px;display:flex;align-items:center;justify-content:center;clip-path:polygon(25% 0,100% 0,100% 100%,0 100%)}
.footer-brand{left:8px;bottom:3px;font-size:9px;font-weight:700;color:var(--green-dark);display:flex;align-items:center;gap:3px}
.footer-brand .dot{width:7px;height:7px;border-radius:50%;background:var(--green)}
</style>
</head>
<body>

<svg width="0" height="0" style="position:absolute" aria-hidden="true">
  <defs>
    <symbol id="ic-grass" viewBox="0 0 20 20"><path d="M2 17 Q4 9 5 6 Q6 12 7 17 M7 17 Q9 7 10 3 Q11 10 12 17 M12 17 Q14 9 15 6 Q16 12 18 17 Z" fill="#fff" stroke="#fff" stroke-width="1"/></symbol>
    <symbol id="ic-flower" viewBox="0 0 20 20"><g fill="none" stroke="#fff" stroke-width="1.4"><circle cx="10" cy="7" r="2"/><circle cx="10" cy="3.5" r="2"/><circle cx="13.5" cy="7" r="2"/><circle cx="6.5" cy="7" r="2"/><circle cx="10" cy="10.5" r="2"/><path d="M10 12.5V19M10 16Q6 14 5 12M10 16Q14 14 15 12"/></g></symbol>
    <symbol id="ic-palm" viewBox="0 0 20 20"><path d="M10 8 Q3 3 1 8 Q5 5 10 8 Q17 3 19 8 Q15 5 10 8 Q8 2 4 2 Q9 3 10 8 Q12 2 16 2 Q11 3 10 8 M9.3 8 L9 19 L11 19 L10.7 8Z" fill="#fff"/></symbol>
    <symbol id="ic-hands" viewBox="0 0 20 20"><g fill="none" stroke="#fff" stroke-width="1.3"><path d="M10 11V5M10 7Q7 6 6 3Q9 3 10 7M10 7Q13 6 14 3Q11 3 10 7"/><path d="M2 10L5 15L8 17V19M18 10L15 15L12 17V19"/></g></symbol>
    <symbol id="ic-shears" viewBox="0 0 20 20"><g fill="none" stroke="#fff" stroke-width="1.4"><path d="M4 18L12 6Q14 3 17 2Q16 6 13 8L6 18"/><circle cx="4" cy="17" r="1.8"/><path d="M8 10L16 14"/></g></symbol>
    <symbol id="ic-sprout" viewBox="0 0 20 20"><g fill="none" stroke="#fff" stroke-width="1.4"><path d="M10 14V6M10 8Q6 7 5 3Q9 3 10 8M10 8Q14 7 15 3Q11 3 10 8"/><ellipse cx="10" cy="16" rx="7" ry="2.5"/></g></symbol>
    <symbol id="ic-pin" viewBox="0 0 10 10"><path d="M5 0a3.5 3.5 0 0 1 3.5 3.5C8.5 6 5 10 5 10S1.5 6 1.5 3.5A3.5 3.5 0 0 1 5 0z" fill="#6fd87f"/></symbol>
    <symbol id="ic-phone" viewBox="0 0 10 10"><path d="M2 0.5L4 2.5L3 4Q4 6 6 7L7.5 6L9.5 8L8 9.5Q3 9 0.5 2Z" fill="#6fd87f"/></symbol>
  </defs>
</svg>

<!-- Page 1 -->
<section class="page p1">
  <div class="abs brand-band"></div>
  <div class="abs contact">
    <div class="division">Landscape and Grounds Maintenance Division</div>
    <div><svg><use href="#ic-pin"/></svg>4120 Willow Creek Road, Lake Harlow, FL 33590</div>
    <div><svg><use href="#ic-phone"/></svg>555-310-0142</div>
    <div><svg><use href="#ic-phone"/></svg>555-610-0388</div>
  </div>
  <div class="abs brand-name"><span class="dot"></span>FernHollow</div>

  <h1 class="abs title" style="left:14px;top:70px">GARDENS ON MARISOL POA &amp; RETAIL</h1>
  <div class="abs month" style="left:268px;top:69px">NOV 2021</div>
  <div class="abs subband" style="top:90px">Landscape, Irrigation &amp; Property Inspection</div>

  <div class="abs item-icon" style="left:12px;top:119px"><span><svg><use href="#ic-grass"/></svg></span></div>
  <div class="abs item-bar" style="left:55px;top:130px">1. GRASSES THROUGHOUT</div>
  <p class="abs item-text" style="left:64px;top:153px">Right now the Muhly grass is blooming and looks great. The crew went around and trimmed them all up so they look fresh and clean. There were some of the types that were not blooming, that we trimmed back farther.</p>
  <div class="abs photo" role="img" aria-label="Ornamental grasses along a building wall" style="left:63px;top:194px;width:159px;height:109px;background:linear-gradient(180deg,#cfcac0,#8a8a7a 60%,#6a6a5e)"></div>
  <div class="abs photo" role="img" aria-label="Pink blooming Muhly grass bed with a young tree" style="left:226px;top:194px;width:101px;height:109px;background:linear-gradient(180deg,#c9d2dc 0%,#8fa07a 40%,#c88aa2 65%,#6e8a4e 100%)"></div>

  <div class="abs item-icon" style="left:12px;top:306px"><span><svg><use href="#ic-flower"/></svg></span></div>
  <div class="abs item-bar" style="left:55px;top:316px">2. FLOWERS</div>
  <p class="abs item-text" style="left:64px;top:342px">Both main entrances are in need of fresh flowers.</p>
  <div class="abs photo" role="img" aria-label="Entrance median bed needing new flowers" style="left:63px;top:359px;width:159px;height:110px;background:linear-gradient(180deg,#d6dde4 0%,#8d8f8a 45%,#6f7a52 70%,#8a7a6e 100%)"></div>

  <div class="abs grass"></div>
  <div class="abs footer-bar">FernHollow Confidential-2021</div>
  <div class="abs page-no">p1</div>
  <div class="abs footer-brand"><span class="dot"></span>FernHollow</div>
</section>

<!-- Page 2 -->
<section class="page p2">
  <h1 class="abs title" style="left:16px;top:10px">GARDENS ON MARISOL POA &amp; RETAIL</h1>
  <div class="abs month" style="left:269px;top:9px">NOV 2021</div>
  <div class="abs subband" style="top:29px">Landscape, Irrigation &amp; Property Inspection</div>

  <div class="abs item-icon" style="left:11px;top:57px"><span><svg><use href="#ic-palm"/></svg></span></div>
  <div class="abs item-bar" style="left:53px;top:68px">3. PALM NEEDS TRIMMING</div>
  <p class="abs item-text" style="left:62px;top:91px">All the Palms could use a trimming, there are dead frons and some hanging seed pods and boots. Let us know if and when you would like to get this scheduled.</p>
  <div class="abs photo" role="img" aria-label="Palm trees lining an entrance drive" style="left:61px;top:120px;width:110px;height:146px;background:linear-gradient(180deg,#dfe4ea 0%,#5f7a44 40%,#7e8074 65%,#9a8a80 100%)"></div>
  <div class="abs photo" role="img" aria-label="Clustered palms beside a crosswalk" style="left:177px;top:120px;width:121px;height:146px;background:linear-gradient(180deg,#e2e6ea 0%,#5d7a46 45%,#8a8c88 75%,#a8a8a6 100%)"></div>

  <div class="abs item-icon" style="left:13px;top:271px"><span><svg><use href="#ic-hands"/></svg></span></div>
  <div class="abs item-bar" style="left:55px;top:282px">4. FILL IN</div>
  <p class="abs item-text" style="left:64px;top:304px">We should fill this corner in where truck run over the corner with additional plants.</p>
  <div class="abs photo" role="img" aria-label="Damaged corner of a curbed planting bed" style="left:62px;top:323px;width:109px;height:145px;background:linear-gradient(180deg,#dde2e8 0%,#8a9a74 35%,#4f6a3a 60%,#8a8888 100%)"></div>

  <div class="abs grass"></div>
  <div class="abs footer-bar">FernHollow Confidential-2021</div>
  <div class="abs page-no">p2</div>
  <div class="abs footer-brand"><span class="dot"></span>FernHollow</div>
</section>

<!-- Page 3 -->
<section class="page p3">
  <h1 class="abs title" style="left:16px;top:10px">GARDENS ON MARISOL POA &amp; RETAIL</h1>
  <div class="abs month" style="left:269px;top:9px">NOV 2021</div>
  <div class="abs subband" style="top:29px">Landscape, Irrigation &amp; Property Inspection</div>

  <div class="abs item-icon" style="left:11px;top:57px"><span><svg><use href="#ic-hands"/></svg></span></div>
  <div class="abs item-bar" style="left:53px;top:68px">5. FILL IN COONTIES</div>
  <p class="abs item-text" style="left:63px;top:91px">Coonties need to be filled in here. As well as side of Six Brothers.</p>
  <div class="abs photo" role="img" aria-label="Parking island with a tree and sparse coonties" style="left:61px;top:110px;width:111px;height:148px;background:linear-gradient(180deg,#dfe6d8 0%,#6f9a4e 35%,#3f6a30 60%,#a9a9a6 100%)"></div>
  <div class="abs photo" role="img" aria-label="Coontie bed beside a building wall" style="left:179px;top:110px;width:107px;height:148px;background:linear-gradient(180deg,#d9d0c2 0%,#b8ad98 35%,#4e6a34 65%,#8a6a46 100%)"></div>

  <div class="abs item-icon" style="left:13px;top:263px"><span><svg><use href="#ic-sprout"/></svg></span></div>
  <div class="abs item-bar" style="left:55px;top:274px">6. MULCH</div>
  <p class="abs item-text" style="left:64px;top:297px">Overall the place could use fresh mulch, or we could just mulch these washed out areas that are an eye sore.</p>
  <div class="abs photo" role="img" aria-label="Washed-out bed along a building needing mulch" style="left:62px;top:328px;width:111px;height:147px;background:linear-gradient(180deg,#dcd6cc 0%,#c4baa8 45%,#8e7e66 70%,#a8a8a6 100%)"></div>

  <div class="abs grass"></div>
  <div class="abs footer-bar">FernHollow Confidential-2021</div>
  <div class="abs page-no">p3</div>
  <div class="abs footer-brand"><span class="dot"></span>FernHollow</div>
</section>

<!-- Page 4 -->
<section class="page p4">
  <h1 class="abs title" style="left:16px;top:10px">GARDENS ON MARISOL POA &amp; RETAIL</h1>
  <div class="abs month" style="left:269px;top:9px">NOV 2021</div>
  <div class="abs subband" style="top:29px">Landscape, Irrigation &amp; Property Inspection</div>

  <div class="abs item-icon" style="left:11px;top:57px"><span><svg><use href="#ic-shears"/></svg></span></div>
  <div class="abs item-bar" style="left:53px;top:68px">7. PRUNING</div>
  <p class="abs item-text" style="left:63px;top:92px">All the little palms have been pruned up to look clean</p>
  <div class="abs photo" role="img" aria-label="Small pruned palms along a building" style="left:61px;top:110px;width:137px;height:151px;background:linear-gradient(180deg,#d8cfbf 0%,#c8bea9 40%,#4f6e3a 65%,#9a9a98 100%)"></div>

  <div class="abs item-icon" style="left:13px;top:263px"><span><svg><use href="#ic-hands"/></svg></span></div>
  <div class="abs item-bar" style="left:55px;top:274px">8. PLANTS FILLING IN</div>
  <p class="abs item-text" style="left:64px;top:297px">The copper plants and Jasmine are all filling in nicely</p>
  <div class="abs photo" role="img" aria-label="Red copper plants along a sidewalk" style="left:61px;top:318px;width:137px;height:159px;background:linear-gradient(180deg,#dfe3e6 0%,#7a8a6a 35%,#a82a3a 65%,#7a2a2e 100%)"></div>
  <div class="abs photo" role="img" aria-label="Copper plant bed under a palm at a median" style="left:205px;top:318px;width:142px;height:159px;background:linear-gradient(180deg,#e2e6ea 0%,#7a8a70 40%,#8a2a32 70%,#8a8a88 100%)"></div>

  <div class="abs grass"></div>
  <div class="abs footer-bar">FernHollow Confidential-2021</div>
  <div class="abs page-no">p4</div>
  <div class="abs footer-brand"><span class="dot"></span>FernHollow</div>
</section>

</body>
</html>
```